Menu redesign of existing iPhone app Lumora

We need a design upgrade for a footer menu of an iPhone app. We need to incorporate a new button for competitions/missions and it should be extremely modern and clean. The central button to create a Lumora cannot be too different as our current users are familiar with its usage.

I have attached screenshots of the curent newsfeed and menu.

Target Market(s)

Photography lovers/ design lovers

Font styles to use
Sans Serif

Requirements
Must have
• Lumora Button,
• Home button,
• My Profile button,
• Find friends button,
• Notifications button,
• Settings button,
• Missions/Competition Button
Nice to have
• Similar Lumora button as existing on the app

```html
<!DOCTYPE html>
<html lang="en">
<head>
<meta charset="utf-8">
<title>Lumora – Footer Menu</title>
<link rel="stylesheet" href="https://fonts.googleapis.com/css2?family=Open+Sans:wght@400;600;700&display=swap">
<style>
  :root {
    --canvas: #eceef2;
    --menu-blue: #4a66cc;
    --menu-blue-deep: #3b55b8;
    --header-blue: rgba(86, 116, 222, 0.88);
    --white: #ffffff;
    --ink: #111418;
    --screen-dark: #0d0f14;
  }
  * { box-sizing: border-box; margin: 0; padding: 0; }
  html, body {
    width: 889px; height: 1200px; overflow: hidden;
    background: var(--canvas);
    font-family: "Open Sans", Arial, sans-serif;
  }
  .canvas {
    position: relative; width: 889px; height: 1200px;
    display: flex; justify-content: center; align-items: center; gap: 29px;
  }
  .screen {
    position: relative; width: 400px; height: 711px; overflow: hidden;
    background: var(--screen-dark); border-radius: 4px;
    box-shadow: 0 10px 30px rgba(20, 30, 60, 0.18);
  }
  .feed-photo {
    position: absolute; inset: 0;
    background: linear-gradient(180deg,
      #2f7d86 0%, #3d8d8d 10%, #6d9a92 28%, #9a9a88 40%,
      #e0784a 50%, #f4b25a 53%, #7d5a6a 58%, #4c4e78 72%, #2c2f52 100%);
  }
  .status-bar {
    position: absolute; top: 0; left: 0; right: 0; height: 22px;
    display: flex; align-items: center; justify-content: space-between;
    padding: 0 10px; font-size: 10px; color: var(--ink); font-weight: 600;
  }
  .status-carrier { letter-spacing: 0.2px; }
  .status-time { position: absolute; left: 50%; transform: translateX(-50%); }
  .status-battery {
    width: 22px; height: 10px; border: 1px solid var(--ink); border-radius: 2px; padding: 1px;
  }
  .status-battery span { display: block; width: 40%; height: 100%; background: var(--ink); }
  .post-header {
    position: absolute; top: 78px; left: 0; right: 0; height: 50px;
    background: var(--header-blue);
    display: flex; align-items: center; padding: 0 12px; color: var(--white);
  }
  .avatar {
    width: 30px; height: 30px; border-radius: 50%; flex: none;
    background: radial-gradient(circle at 40% 40%, #c9a36a, #7a6a4a);
    border: 1px solid rgba(255,255,255,.6);
  }
  .post-meta { margin-left: 9px; line-height: 1.2; }
  .post-author { font-size: 12px; font-weight: 700; }
  .post-author .badge { font-weight: 600; margin-left: 6px; }
  .post-time { font-size: 8.5px; opacity: .9; }
  .post-actions { margin-left: auto; display: flex; gap: 8px; align-items: center; }
  .footer-menu { position: absolute; left: 0; bottom: 0; width: 400px; display: block; }
  .menu-label { font-family: "Open Sans", Arial, sans-serif; font-size: 12px; fill: var(--white); }
  .counter { font-family: "Open Sans", Arial, sans-serif; font-size: 9px; font-weight: 700; }
</style>
</head>
<body>
<svg width="0" height="0" style="position:absolute" aria-hidden="true">
  <defs>
    <g id="icon-ring"><circle r="13" fill="none" stroke="#fff" stroke-width="2"/></g>
    <g id="icon-up"><use href="#icon-ring"/><path d="M0 6V-6M-5-1L0-6L5-1" fill="none" stroke="#fff" stroke-width="2" stroke-linecap="round" stroke-linejoin="round"/></g>
    <g id="icon-home"><use href="#icon-ring"/><path d="M-7 0L0-6.5L7 0M-4.5-2V6H4.5V-2" fill="none" stroke="#fff" stroke-width="2" stroke-linejoin="round"/></g>
    <g id="icon-profile"><use href="#icon-ring"/><circle cy="-3" r="3.5" fill="#fff"/><path d="M-6 7A6 6 0 0 1 6 7Z" fill="#fff"/></g>
    <g id="icon-friends"><use href="#icon-ring"/><circle cx="-3" cy="-3" r="3" fill="#fff"/><circle cx="4" cy="-2" r="2.5" fill="#fff"/><path d="M-8 6A5 5 0 0 1 2 6Z M1 6A4 4 0 0 1 8 6Z" fill="#fff"/></g>
    <g id="icon-chat"><use href="#icon-ring"/><rect x="-7" y="-6" width="11" height="8" rx="2" fill="#fff"/><rect x="-3" y="-2" width="10" height="7" rx="2" fill="none" stroke="#fff" stroke-width="1.5"/></g>
    <g id="icon-settings"><use href="#icon-ring"/><circle r="5.5" fill="none" stroke="#fff" stroke-width="3" stroke-dasharray="2.2 2.1"/><circle r="2.5" fill="none" stroke="#fff" stroke-width="1.5"/></g>
    <g id="lumora-button">
      <circle r="34" fill="var(--menu-blue)"/>
      <circle r="25" fill="#fff"/>
      <circle r="21" fill="none" stroke="var(--menu-blue)" stroke-width="2"/>
      <polygon points="-5,-12 5,-12 12,-5 12,5 5,12 -5,12 -12,5 -12,-5" fill="var(--menu-blue)"/>
    </g>
    <g id="icon-star-count">
      <path d="M11 1L14 8L21 8.5L16 13L17.5 20L11 16.5L4.5 20L6 13L1 8.5L8 8Z" fill="none" stroke="#fff" stroke-width="1.6" stroke-linejoin="round"/>
    </g>
  </defs>
</svg>

<main class="canvas">
  <!-- Feed with collapsed menu -->
  <section class="screen screen--collapsed">
    <div class="feed-photo" role="img" aria-label="Feed photo: silhouette of a person on a beach at sunset, sea above"></div>
    <div class="status-bar">
      <span class="status-carrier">●●●●● NEBULA</span>
      <span class="status-time">10:27</span>
      <span class="status-battery"><span></span></span>
    </div>
    <header class="post-header">
      <div class="avatar" role="img" aria-label="User avatar photo"></div>
      <div class="post-meta">
        <div class="post-author">Elio <span class="badge">★ Staff Pick</span></div>
        <div class="post-time">15 hours ago</div>
      </div>
      <div class="post-actions">
        <svg width="22" height="22" viewBox="0 0 22 22"><use href="#icon-star-count"/><text class="counter" x="11" y="14" text-anchor="middle" fill="#fff">58</text></svg>
        <svg width="24" height="22" viewBox="0 0 24 22"><path d="M12 2C6.5 2 2 5.5 2 10s4.5 8 10 8l1 0 5 3-1-4c3-1.5 5-4 5-7 0-4.5-4.5-8-10-8Z" fill="none" stroke="#fff" stroke-width="1.6"/><text class="counter" x="12" y="13" text-anchor="middle" fill="#fff">0</text></svg>
      </div>
    </header>
    <svg class="footer-menu" width="400" height="96" viewBox="0 0 400 96">
      <rect x="0" y="36" width="400" height="60" fill="var(--menu-blue)"/>
      <use href="#lumora-button" x="200" y="40"/>
      <use href="#icon-up" x="42" y="68"/>
      <use href="#icon-home" x="358" y="68"/>
    </svg>
  </section>

  <!-- Feed with expanded menu -->
  <section class="screen screen--expanded">
    <div class="feed-photo" role="img" aria-label="Feed photo: silhouette of a person on a beach at sunset, sea above"></div>
    <div class="status-bar">
      <span class="status-carrier">●●●●● NEBULA</span>
      <span class="status-time">10:27</span>
      <span class="status-battery"><span></span></span>
    </div>
    <header class="post-header">
      <div class="avatar" role="img" aria-label="User avatar photo"></div>
      <div class="post-meta">
        <div class="post-author">Elio <span class="badge">★ Staff Pick</span></div>
        <div class="post-time">15 hours ago</div>
      </div>
      <div class="post-actions">
        <svg width="22" height="22" viewBox="0 0 22 22"><use href="#icon-star-count"/><text class="counter" x="11" y="14" text-anchor="middle" fill="#fff">58</text></svg>
        <svg width="24" height="22" viewBox="0 0 24 22"><path d="M12 2C6.5 2 2 5.5 2 10s4.5 8 10 8l1 0 5 3-1-4c3-1.5 5-4 5-7 0-4.5-4.5-8-10-8Z" fill="none" stroke="#fff" stroke-width="1.6"/><text class="counter" x="12" y="13" text-anchor="middle" fill="#fff">0</text></svg>
      </div>
    </header>
    <svg class="footer-menu" width="400" height="200" viewBox="0 0 400 200">
      <defs>
        <linearGradient id="panel-fade" x1="0" y1="0" x2="0" y2="1">
          <stop offset="0" stop-color="var(--menu-blue)"/>
          <stop offset="1" stop-color="var(--menu-blue-deep)"/>
        </linearGradient>
      </defs>
      <path d="M0 74L200 40L400 74V200H0Z" fill="url(#panel-fade)"/>
      <text class="menu-label" x="70" y="78" text-anchor="middle" transform="rotate(-9.6 70 78)">Missions</text>
      <text class="menu-label" x="330" y="78" text-anchor="middle" transform="rotate(9.6 330 78)">Competition</text>
      <use href="#lumora-button" x="200" y="60"/>
      <use href="#icon-up" x="80" y="115"/>
      <use href="#icon-home" x="320" y="115"/>
      <use href="#icon-profile" x="80" y="165"/>
      <use href="#icon-friends" x="160" y="165"/>
      <use href="#icon-chat" x="240" y="165"/>
      <use href="#icon-settings" x="320" y="165"/>
    </svg>
  </section>
</main>
</body>
</html>
```